Silver MarlinJuice Company from Germany needs a Web Design

Hey Guys,

We need a Great Web Design I Hope we get nice Designs.
I put our company Logo in the Files.
Our Juice is Very Healthy and we don't use Sugar or other stuff it's 100% Natural Juice.
We are a German Company
Updates

I have a good Design already , but when someone works on a design, i will wait until you send it to me.

Industry/Entity Type

It Company

Coding

Coded - Design and coding required

Number of Pages Required

1 page

Requirements
Must have
• It has to be something with Vegetables: Apple, Carrots, courgette, fennel, beetroot, orange, salads, lemons, nettle. We producing the juice with these Vegetables and fruits.
Nice to have
• I Put a couple designs in the files i like Designs ,when you go on a Website and you are not confused :)

```html
<!DOCTYPE html>
<html lang="en">
<head>
<meta charset="utf-8">
<title>Silver Marlin Juice</title>
<link href="https://fonts.googleapis.com/css2?family=Open+Sans:wght@400;600;700&family=Oswald:wght@500;600&family=Dancing+Script:wght@600&display=swap" rel="stylesheet">
<style>
:root{
  --green:#79b52c;
  --green-dark:#5f9a1c;
  --green-light:#a6d85a;
  --ink:#333;
  --muted:#777;
  --line:#dcdcdc;
  --page:#f4f4f4;
  --card:#fff;
  --footer:#1e1e1e;
  --footer-text:#bdbdbd;
  --footer-bar:#151515;
}
*{box-sizing:border-box;margin:0;padding:0}
html,body{width:809px;height:1200px;overflow:hidden}
body{background:var(--page);font-family:"Open Sans",Arial,sans-serif;color:var(--ink);font-size:8px;line-height:1.45;position:relative}
.wrap{position:absolute;left:95px;width:620px}

/* header */
.site-header{position:absolute;top:0;left:0;width:809px;height:140px;background:#fff}
.brand{position:absolute;left:95px;top:22px;display:flex;align-items:center;gap:8px}
.brand-dot{width:26px;height:26px;border-radius:50%;background:var(--green)}
.brand-name{font-size:17px;font-weight:700;color:var(--green);line-height:1}
.search{position:absolute;left:551px;top:36px;width:135px;height:18px;border:1px solid var(--line);background:#fff;font-size:8px;color:var(--muted);padding:3px 6px}
.search-btn{position:absolute;left:686px;top:36px;width:18px;height:18px;background:var(--green)}
.corner-leaves{position:absolute;right:0;top:0;width:80px;height:70px;background:radial-gradient(circle at 70% 30%,#9fd24a,#5f9a1c 60%,rgba(255,255,255,0) 72%)}
.main-nav{position:absolute;left:95px;top:100px;width:620px;height:19px;background:linear-gradient(var(--green-light),var(--green));display:flex;justify-content:space-around;align-items:center}
.main-nav a{color:#fff;font-size:8px;font-weight:600;text-decoration:none;letter-spacing:.3px}

/* hero */
.hero{top:150px;height:268px;background:#fff;border:1px solid var(--line);padding:5px}
.hero-media{position:relative;height:100%;background:linear-gradient(90deg,#6fae2a 0%,#cfe8a8 35%,#f4f8ec 55%,#f7d38b 75%,#f29a3a 90%,#c9e07c 100%);overflow:hidden}
.hero-title{position:absolute;left:38px;top:100px;font-family:Oswald,Arial,sans-serif;color:#fff;font-size:26px;font-weight:600;line-height:1.1;letter-spacing:.5px}
.hero-dots{position:absolute;left:14px;bottom:10px;display:flex;gap:4px}
.hero-dots span{width:6px;height:6px;border-radius:50%;background:rgba(255,255,255,.6)}
.hero-dots span:first-child{background:#fff}

/* section labels */
.section-label{height:14px;display:flex;align-items:center}
.section-label .tab{background:var(--green);color:#fff;font-weight:700;font-size:8px;padding:1px 10px 1px 8px;height:14px;line-height:12px;clip-path:polygon(0 0,100% 0,92% 50%,100% 100%,0 100%)}
.section-label .rule{flex:1;height:1px;background:var(--line)}
.arrows{display:flex;gap:4px;margin-left:6px}
.arrows svg{width:8px;height:10px}

/* welcome */
.welcome{top:440px}
.welcome-body{display:flex;gap:14px;margin-top:28px}
.welcome-photo{width:125px;height:75px;background:linear-gradient(135deg,#f2f2f2,#b7c98e 55%,#6b5236);flex:none}
.welcome-text{color:var(--muted);font-size:8px;padding-top:2px}

/* products */
.products{top:594px}
.product-grid{display:flex;justify-content:space-between;margin-top:22px}
.product{width:128px;height:180px;background:var(--card);border:1px solid var(--line);text-align:center;padding-top:14px}
.bottle{width:30px;height:100px;margin:0 auto;border-radius:6px 6px 4px 4px}
.bottle.apple{background:linear-gradient(#f0a060,#e8722a)}
.bottle.courgette{background:linear-gradient(#b6e36a,#7dc23a)}
.bottle.orange{background:linear-gradient(#ffd36b,#f5a623)}
.bottle.salade{background:linear-gradient(#f7ef8a,#e7d948)}
.product h3{font-size:8px;font-weight:700;margin-top:14px;color:var(--ink)}
.product p{color:var(--muted);font-size:7px;padding:2px 14px 0;line-height:1.35}

/* testimonials */
.testimonials{top:842px}
.quote-row{display:flex;justify-content:space-between;margin-top:22px}
.quote{width:300px;background:#fff;border:1px solid var(--line);height:88px;padding:12px 10px;display:flex;gap:10px}
.avatar{width:34px;height:42px;flex:none;background:linear-gradient(#d9d9d9,#9a9a9a)}
.quote p{color:var(--muted);font-size:7.5px}
.signature{font-family:"Dancing Script",cursive;color:var(--green-dark);font-size:11px;margin-top:8px;padding-left:2px}
.sig-row{display:flex}
.sig-row .signature{width:300px;margin-left:0}
.sig-row .signature + .signature{margin-left:20px}

/* footer */
.site-footer{position:absolute;left:0;top:1000px;width:809px;height:200px;background:var(--footer)}
.footer-cols{position:absolute;left:95px;top:18px;width:620px;display:flex;justify-content:space-between}
.footer-col{width:130px}
.footer-col h4{font-family:"Dancing Script",cursive;font-weight:600;color:#fff;font-size:13px;margin-bottom:7px}
.footer-col li{list-style:none;color:var(--footer-text);font-size:7px;line-height:1.75}
.social li{display:flex;align-items:center;gap:6px;margin-bottom:4px}
.social .dot{width:12px;height:12px;border-radius:50%;background:#5a5a5a;flex:none}
.footer-bar{position:absolute;left:0;bottom:0;width:809px;height:22px;background:var(--footer-bar);color:#8a8a8a;font-size:7px;text-align:center;line-height:22px}
</style>
</head>
<body>

<header class="site-header">
  <div class="brand"><span class="brand-dot"></span><span class="brand-name">Silver Marlin</span></div>
  <div class="search">Search</div>
  <div class="search-btn"></div>
  <div class="corner-leaves" role="img" aria-label="Fresh green leaves in the corner"></div>
  <nav class="main-nav">
    <a href="#">HOME</a><a href="#">ABOUT US</a><a href="#">SPECIALS</a><a href="#">ALL PRODUCTS</a><a href="#">REVIEWS</a><a href="#">CONTACTS</a><a href="#">FAQS</a>
  </nav>
</header>

<section class="wrap hero">
  <div class="hero-media" role="img" aria-label="Bottles of fresh juice in a row beside green leaves">
    <div class="hero-title">SILVER MARLIN<br>JUICE</div>
    <div class="hero-dots"><span></span><span></span><span></span><span></span></div>
  </div>
</section>

<section class="wrap welcome">
  <div class="section-label"><span class="tab">WELCOME</span><span class="rule"></span></div>
  <div class="welcome-body">
    <div class="welcome-photo" role="img" aria-label="Hands holding a young plant growing in soil"></div>
    <p class="welcome-text">Fresh pressed every morning from apples, carrots, courgette, fennel, beetroot and oranges grown by farmers we know. No added sugar, no concentrates and no preservatives, just one hundred percent natural juice. We bottle each batch within hours of harvest so every glass keeps the colour, taste and vitamins of the field. Discover the range and find your favourite blend.</p>
  </div>
</section>

<section class="wrap products">
  <div class="section-label"><span class="tab">PRODUCTS</span><span class="rule"></span>
    <span class="arrows">
      <svg viewBox="0 0 8 10"><path d="M6 1 2 5l4 4" fill="none" stroke="#aaa" stroke-width="1.5"/></svg>
      <svg viewBox="0 0 8 10"><path d="M2 1l4 4-4 4" fill="none" stroke="#aaa" stroke-width="1.5"/></svg>
    </span>
  </div>
  <div class="product-grid">
    <article class="product"><div class="bottle apple" role="img" aria-label="Bottle of apple juice"></div><h3>APPLE</h3><p>Crisp orchard apples, cold pressed, no sugar added.</p></article>
    <article class="product"><div class="bottle courgette" role="img" aria-label="Bottle of courgette juice"></div><h3>COURGETTE</h3><p>Mild green courgette with a hint of fennel.</p></article>
    <article class="product"><div class="bottle orange" role="img" aria-label="Bottle of orange juice"></div><h3>ORANGE</h3><p>Sunny oranges squeezed fresh for a bright start.</p></article>
    <article class="product"><div class="bottle salade" role="img" aria-label="Bottle of salad juice"></div><h3>SALADE</h3><p>Leafy greens and lemon for a light lift.</p></article>
  </div>
</section>

<section class="wrap testimonials">
  <div class="section-label"><span class="tab">TESTIMONIALS</span><span class="rule"></span></div>
  <div class="quote-row">
    <blockquote class="quote"><div class="avatar" role="img" aria-label="Customer portrait"></div><p>I drink the carrot and beetroot blend every morning. It tastes like it came straight from the garden and keeps me going all day long.</p></blockquote>
    <blockquote class="quote"><div class="avatar" role="img" aria-label="Customer portrait"></div><p>Finally a juice without hidden sugar. My children love the apple one and I love knowing exactly what is inside every single bottle.</p></blockquote>
  </div>
  <div class="sig-row"><div class="signature">Name Here</div><div class="signature">Name Here</div></div>
</section>

<footer class="site-footer">
  <div class="footer-cols">
    <div class="footer-col"><h4>Categories</h4><ul><li>Home</li><li>About Us</li><li>Products</li><li>Latest News</li><li>Login</li><li>Join Us</li></ul></div>
    <div class="footer-col"><h4>Get in Touch</h4><ul class="social"><li><span class="dot"></span>Chatter</li><li><span class="dot"></span>Facepage</li><li><span class="dot"></span>RSS</li><li><span class="dot"></span>Email</li></ul></div>
    <div class="footer-col"><h4>Services</h4><ul><li>Shipping Methods</li><li>Return Policy</li><li>Track Your Orders</li><li>Terms &amp; Privacy</li><li>Secure Payments</li><li>FAQ</li></ul></div>
    <div class="footer-col"><h4>Contact Us</h4><ul><li>Address</li><li>Street name</li><li>Street no, 12345 City</li><li>123 456 7890</li><li>hello@silvermarlinjuice.de</li></ul></div>
  </div>
  <div class="footer-bar">© 2015 Silver Marlin Juice. All Rights Reserved</div>
</footer>

</body>
</html>
```